Property risk and finance brokerage company needs a business card design

Tarn Financial requires a business card design. Please integrate existing logo (refer uploaded file).
hex codes used on logo #002649 #008ED6 #444F51 #ADAFAA
font used - Cinzel
Contact information
Roslyn Venterelli
Director
Mobile: 0471 385 902
email: r.venterelli@tarnfinancial.com.au
website: www.tarnfinancial.com.au
CRN : 815390
PO Box 547
merrowvale, eastmere, 3199
Horizontal orientation please

```html
<!DOCTYPE html>
<html lang="en">
<head>
<meta charset="utf-8">
<title>Tarn Financial – Business Card</title>
<link rel="stylesheet" href="https://fonts.googleapis.com/css2?family=Cinzel:wght@400;700&family=Questrial&display=swap">
<style>
  :root {
    --navy: #002649;
    --navy-soft: #0f3a6b;
    --blue: #008ED6;
    --slate: #444F51;
    --stone: #ADAFAA;
    --muted: #8a8f91;
    --paper: #ffffff;
    --backdrop: #e6e7e8;
  }
  * { margin: 0; padding: 0; box-sizing: border-box; }
  html, body {
    width: 1000px; height: 1200px; overflow: hidden;
    background: var(--backdrop);
  }
  .canvas { position: relative; width: 1000px; height: 1200px; }
  .card {
    position: absolute; left: 70px; width: 860px; height: 491px;
    box-shadow: 0 6px 24px rgba(0,0,0,0.18);
    overflow: hidden;
  }
  /* Front */
  .card-front { top: 80px; background: var(--paper); }
  .band { position: absolute; height: 46px; }
  .band-top { left: 62px; top: 24px; width: 270px; background: var(--navy-soft); }
  .band-bottom { left: 90px; bottom: 0; width: 270px; background: var(--navy); }
  .brand {
    position: absolute; left: 70px; top: 222px;
    display: flex; align-items: center; gap: 14px;
  }
  .brand-dot { width: 40px; height: 40px; border-radius: 50%; background: var(--blue); flex: none; }
  .brand-name {
    font-family: 'Cinzel', serif; font-weight: 400; color: var(--navy);
    font-size: 34px; line-height: 1.05; letter-spacing: 1px;
  }
  .contact { position: absolute; left: 370px; top: 120px; color: var(--navy); }
  .person-name {
    font-family: 'Cinzel', serif; font-weight: 700; font-size: 24px; letter-spacing: 0.5px;
  }
  .person-role {
    font-family: 'Cinzel', serif; font-weight: 400; font-size: 21px; color: var(--muted);
    margin-top: 2px;
  }
  .details {
    font-family: 'Questrial', sans-serif; font-size: 20px; line-height: 1.3; margin-top: 46px;
  }
  .postal { font-family: 'Questrial', sans-serif; font-size: 20px; margin-top: 28px; }
  /* Back */
  .card-back {
    top: 630px;
    background: radial-gradient(ellipse at 50% 45%, var(--blue) 0%, #0a5a9a 35%, var(--navy) 85%);
    display: flex; flex-direction: column; align-items: center; justify-content: center;
    color: var(--paper);
  }
  .back-brand { display: flex; align-items: center; gap: 22px; }
  .back-brand .brand-dot { background: var(--paper); width: 54px; height: 54px; }
  .back-brand .brand-name { color: var(--paper); font-size: 52px; }
  .website {
    font-family: 'Cinzel', serif; font-size: 20px; letter-spacing: 2px; margin-top: 44px;
  }
</style>
</head>
<body>
<main class="canvas">
  <section class="card card-front">
    <div class="band band-top"></div>
    <div class="band band-bottom"></div>
    <div class="brand">
      <span class="brand-dot"></span>
      <div class="brand-name">TARN<br>FINANCIAL</div>
    </div>
    <div class="contact">
      <div class="person-name">Roslyn Venterelli, BCom, MFAA</div>
      <div class="person-role">Director</div>
      <div class="details">
        0471 385 902<br>
        r.venterelli@tarnfinancial.com.au<br>
        Credit Rep No: CRN 815390
      </div>
      <div class="postal">PO Box 547 merrowvale, eastmere, 3199</div>
    </div>
  </section>
  <section class="card card-back">
    <div class="back-brand">
      <span class="brand-dot"></span>
      <div class="brand-name">TARN<br>FINANCIAL</div>
    </div>
    <div class="website">WWW.TARNFINANCIAL.COM.AU</div>
  </section>
</main>
</body>
</html>
```